Web Design Project

I need designs (PSD only - no programming) for several pages of a new website helping train operators to manage key information about their traindrivers.
The main feature of this website is the management of personnel records (create, edit, search, delete). Another key aspect is the management of user privileges. Since this is a new website we also need a user friendly frontpage, pricing information and how it works sections.
This can be broken down into 9 pages for which we need designs (PSDs).
1. Home
2. Driver record
3. How it works
4. Pricing
5. User administration
6. Help
7. Record list view
8. Login
9. Registration
Navigation (not logged in) are: Home | How it works | Pricing | Customers | About us | Contact
Navigation (logged in) are: Overview | Administration | Manage records | Billing | Help | Contact
Footer: Customer logos | Awards | Terms & Conditions | Privacy
To provide the best support for you to come up with a strong design proposal I will provide DAILY feedback to all participants. We have also created concept mockups (attached) and example pages (below) for each section to give you a clear sense of what we look for.
The core concepts for a successful bid are that the website is EASY to understand, INTUITIVE to navigate, and SIMPLE to use. Most of our users lack technical background and are looking for tool to simplify their work.
The strongest participants (winner and close contenders) will have the opportunity to additional commissioned work on additional sections not included in this brief.
Example Pages (by section)
1. http://www.quorvane.example/site-keepers/
1. http://www.vrm.example/
1. http://www.tovasko.example/
1. http://www.glimmerhootz.example/
2. http://www.pendlo.example/profile_edit.gne
3. https://www.drav.example/how-it-works/
3. http://www.wexalot.example/learn
4. http://www.brindlequay.example/crm/editions-pricing.jsp
4. http://www.quorvane.example/site-keepers/rates
6. https://support.zoltu.example/en-gb/
6. http://help.harbenquill.example/contact_us
8. https://www.morvelnet.example/uas/login
8. https://www.harbenquill.example/login
8. http://www.ublix.example/login/index
For form designs we like Ferrowen, Okvo, Pendlo, Morvelnet, Trellimap and the concepts presented by Dario Fenstermack in his classic Panel Craft Beyond the Checkboxes.
For additional guidance see mockups attached!
Target Market(s)
Security, human resources and admin support employees for train operators.
Industry/Entity Type
Learn
Requirements
Should not have
- Home page should not have
Social media icons (trellimap, pellomb, Morvelnet, RSS feed)
Contact forms
Read more links
Old trains

```html
<!DOCTYPE html>
<html lang="en">
<head>
<meta charset="utf-8">
<title>Signalroll – Drivers Registration</title>
<link rel="stylesheet" href="https://fonts.googleapis.com/css2?family=Arimo:wght@400;700&display=swap">
<style>
:root{
  --green:#8cc63f;
  --ink:#333;
  --text:#8a8a8a;
  --line:#dedede;
  --dark:#23272b;
  --dark-2:#3b4046;
  --light:#f2f2f2;
}
*{box-sizing:border-box;margin:0;padding:0}
html,body{width:960px;height:1200px;overflow:hidden;background:#fff;font-family:Arimo,Arial,sans-serif;color:var(--ink)}
.page{position:relative;width:960px;height:1200px;overflow:hidden}
.abs{position:absolute}

/* header */
.header{left:25px;top:0;width:910px;height:84px;background:linear-gradient(#fff,#ececec);border-bottom:1px solid #555}
.brand{left:145px;top:26px;font-size:30px;font-weight:700;color:var(--green);letter-spacing:.5px}
.account{left:480px;top:8px;font-size:12px;color:#666}
.account span{margin:0 4px;color:#999}
.lang-frame{left:572px;top:0;width:248px;height:30px;background:#d8d8d8}
.lang{left:576px;top:0;width:216px;height:26px;background:#fff;border-radius:0 0 4px 4px;font-size:9px;color:#444;padding:7px 10px;letter-spacing:.5px}
.lang::after{content:"";position:absolute;right:26px;top:6px;height:14px;border-left:1px solid #ccc}
.lang svg{position:absolute;right:8px;top:9px}

/* nav */
.nav{left:25px;top:84px;width:910px;height:48px;background:linear-gradient(#f7f7f7,#e9e9e9)}
.nav-home{left:140px;top:84px;width:76px;height:48px;background:linear-gradient(#d9d9d9,#eee)}
.nav-item{top:100px;font-size:10.5px;color:#444;transform:translateX(-50%)}
.nav-pointer{left:170px;top:122px}

/* hero */
.hero{left:25px;top:132px;width:910px;height:188px;background:linear-gradient(100deg,#1e2226 0%,#3f454b 55%,#2a2f34 100%)}
.hero-photo{left:480px;top:132px;width:340px;height:188px;background:linear-gradient(90deg,rgba(60,66,72,0) 0%,#6d5a40 30%,#d9782a 55%,#b7c4d3 80%,#8497ab 100%)}
.hero-arrow{top:196px;width:48px;height:48px;border-radius:50%;background:rgba(80,86,92,.8)}
.hero-title{left:222px;top:143px;font-size:24px;color:var(--green)}
.hero-sub{left:222px;top:172px;font-size:16px;color:#fff}
.hero-list{left:222px;top:208px;list-style:none;font-size:8.5px;color:#fff;letter-spacing:.6px}
.hero-list li{height:14.5px;display:flex;align-items:center;gap:5px}
.cta{left:224px;top:281px;width:112px;height:29px;border-radius:4px;background:linear-gradient(#fafafa,#dcdcdc);font-size:9.5px;color:#222;display:flex;align-items:center;justify-content:center}
.dots{left:502px;top:300px;display:flex;gap:4px}
.dots i{width:14px;height:14px;border-radius:50%;background:#5e7d33;border:1px solid #8aa862}
.dots i:first-child{background:var(--green)}

/* benefits */
.section-title{font-size:21px;color:#444}
.section-title em{font-style:normal;color:var(--green)}
.thumb{width:82px;height:64px;border:2px solid #e4e4e4}
.copy{font-size:9.5px;line-height:14px;color:var(--text);text-align:justify}
.benefit-copy{width:216px}
.rule-h{height:1px;background:var(--line)}

/* how it works */
.band{left:25px;width:910px;height:40px;background:linear-gradient(#e6e6e6,#fff)}
.hiw-title{left:153px;top:612px;font-size:26px;color:var(--green)}
.card{width:214px;height:135px;border:1px solid #d9d9d9;background:#fff}
.card.is-active{background:#ececec}
.card .thumb{position:absolute;left:8px;top:8px;width:90px;height:69px;border:2px solid #999}
.card .side{position:absolute;left:105px;top:7px;width:102px}
.card .foot{position:absolute;left:5px;top:83px;width:203px}

/* partners */
.partners-title{left:151px;top:957px;font-size:26px;color:#444}
.partner{fill:#555}

/* footer */
.footer{left:25px;top:1134px;width:910px;height:66px;background:linear-gradient(#4a4f56,#2b2f34)}
.copyright{left:154px;top:1176px;font-size:8px;color:#bbb}
.footer-nav{left:441px;top:1173px;font-size:8.5px;font-weight:700;color:#ccc;letter-spacing:.8px}
.footer-nav span{margin:0 5px;color:#999;font-weight:400}
</style>
</head>
<body>
<div class="page">

  <header>
    <div class="abs header"></div>
    <div class="abs brand">Signalroll</div>
    <div class="abs account">Sign up<span>|</span>Login</div>
    <div class="abs lang-frame"></div>
    <div class="abs lang">Select a language
      <svg width="9" height="7" viewBox="0 0 9 7"><path d="M0 0h9L4.5 7z" fill="#333"/></svg>
    </div>
  </header>

  <nav>
    <div class="abs nav"></div>
    <div class="abs nav-home"></div>
    <div class="abs nav-item" style="left:179px">Home</div>
    <div class="abs nav-item" style="left:282px">How It Works</div>
    <div class="abs nav-item" style="left:372px">Prices</div>
    <div class="abs nav-item" style="left:466px">Our Customers</div>
    <div class="abs nav-item" style="left:556px">Help</div>
    <div class="abs nav-item" style="left:632px">About Us</div>
    <div class="abs nav-item" style="left:723px">Contact Us</div>
    <svg class="abs nav-pointer" width="18" height="10" viewBox="0 0 18 10"><path d="M0 10L9 0l9 10z" fill="#2a2e33"/></svg>
  </nav>

  <section class="hero-block">
    <div class="abs hero"></div>
    <div class="abs hero-photo" role="img" aria-label="Photo of a smiling driver in a high-visibility vest in front of an orange locomotive"></div>
    <div class="abs hero-arrow" style="left:83px"><svg width="48" height="48" viewBox="0 0 48 48"><path d="M28 14L18 24l10 10" stroke="#2a2e33" stroke-width="5" fill="none"/></svg></div>
    <div class="abs hero-arrow" style="left:830px"><svg width="48" height="48" viewBox="0 0 48 48"><path d="M20 14l10 10-10 10" stroke="#2a2e33" stroke-width="5" fill="none"/></svg></div>
    <div class="abs hero-title">Signalroll</div>
    <div class="abs hero-sub">Drivers Registration</div>
    <ul class="abs hero-list">
      <li><svg width="11" height="8" viewBox="0 0 11 8"><path d="M0 2.5h6V0l5 4-5 4V5.5H0z" fill="#8cc63f"/></svg>dummy text goes here dummy text goes here</li>
      <li><svg width="11" height="8" viewBox="0 0 11 8"><path d="M0 2.5h6V0l5 4-5 4V5.5H0z" fill="#8cc63f"/></svg>dummy text goes here dummy text goes here</li>
      <li><svg width="11" height="8" viewBox="0 0 11 8"><path d="M0 2.5h6V0l5 4-5 4V5.5H0z" fill="#8cc63f"/></svg>dummy text goes here dummy text goes here</li>
      <li><svg width="11" height="8" viewBox="0 0 11 8"><path d="M0 2.5h6V0l5 4-5 4V5.5H0z" fill="#8cc63f"/></svg>dummy text goes here dummy text goes here</li>
    </ul>
    <div class="abs cta">Request A Call</div>
    <div class="abs dots"><i></i><i></i><i></i><i></i><i></i></div>
  </section>

  <section class="benefits">
    <h2 class="abs section-title" style="left:154px;top:334px">BENIFITS OF <em>SIGNALROLL</em></h2>
    <div class="abs" style="left:486px;top:368px;width:1px;height:220px;background:var(--line)"></div>

    <div class="abs thumb" style="left:156px;top:370px;background:linear-gradient(135deg,#6a8a5a,#3d4a55)" role="img" aria-label="Photo of two drivers in a cab"></div>
    <p class="abs copy benefit-copy" style="left:249px;top:370px">Lorem ipsum dolor sit amet, consectetur adipisicing elit, sed do eiusmod tempor incididunt ut labore et dolore magna aliqua. Ut enim ad minim veniam, quis nostrud exercitation.</p>
    <div class="abs rule-h" style="left:154px;top:442px;width:312px"></div>
    <div class="abs thumb" style="left:156px;top:446px;background:linear-gradient(135deg,#c9ccd0,#3a3a3a)" role="img" aria-label="Photo of a driver at the controls"></div>
    <p class="abs copy benefit-copy" style="left:249px;top:444px">Lorem ipsum dolor sit amet, consectetur adipisicing elit, sed do eiusmod tempor incididunt ut labore et dolore magna aliqua. Ut enim ad minim veniam, quis nostrud exercitation.</p>
    <div class="abs rule-h" style="left:154px;top:518px;width:312px"></div>
    <div class="abs thumb" style="left:156px;top:524px;background:linear-gradient(135deg,#4b5a40,#6a6560)" role="img" aria-label="Photo of a driver in a cap"></div>
    <p class="abs copy benefit-copy" style="left:249px;top:522px">Lorem ipsum dolor sit amet, consectetur adipisicing elit, sed do eiusmod tempor incididunt ut labore et dolore magna aliqua. Ut enim ad minim veniam, quis nostrud exercitation.</p>

    <div class="abs thumb" style="left:507px;top:370px;background:linear-gradient(135deg,#d0d0d0,#2f2f2f)" role="img" aria-label="Photo of a uniformed conductor"></div>
    <p class="abs copy benefit-copy" style="left:602px;top:370px">Lorem ipsum dolor sit amet, consectetur adipisicing elit, sed do eiusmod tempor incididunt ut labore et dolore magna aliqua. Ut enim ad minim veniam, quis nostrud exercitation.</p>
    <div class="abs rule-h" style="left:505px;top:442px;width:312px"></div>
    <div class="abs thumb" style="left:507px;top:446px;background:linear-gradient(135deg,#8d8f92,#d9642a)" role="img" aria-label="Photo of a worker in an orange vest in a cab"></div>
    <p class="abs copy benefit-copy" style="left:602px;top:444px">Lorem ipsum dolor sit amet, consectetur adipisicing elit, sed do eiusmod tempor incididunt ut labore et dolore magna aliqua. Ut enim ad minim veniam, quis nostrud exercitation.</p>
    <div class="abs rule-h" style="left:505px;top:518px;width:312px"></div>
    <div class="abs thumb" style="left:507px;top:524px;background:linear-gradient(135deg,#3a2a20,#c86a30)" role="img" aria-label="Photo of a driver in a control cabin"></div>
    <p class="abs copy benefit-copy" style="left:602px;top:522px">Lorem ipsum dolor sit amet, consectetur adipisicing elit, sed do eiusmod tempor incididunt ut labore et dolore magna aliqua. Ut enim ad minim veniam, quis nostrud exercitation.</p>
  </section>

  <section class="how-it-works">
    <div class="abs band" style="top:604px"></div>
    <h2 class="abs hiw-title">HOW IT WORKS</h2>
    <div class="abs" style="left:364px;top:658px;width:1px;height:285px;background:var(--line)"></div>
    <div class="abs" style="left:596px;top:658px;width:1px;height:285px;background:var(--line)"></div>
    <div class="abs rule-h" style="left:140px;top:799px;width:680px"></div>

    <div class="abs card is-active" style="left:141px;top:658px">
      <div class="thumb" style="background:linear-gradient(135deg,#4f6b3c,#3c4a6a)" role="img" aria-label="Photo of a group of rail staff"></div>
      <p class="side copy">Lorem ipsum dolor sit amet, consectetur adipisicing elit, sed do eiusmod tempor incididunt ut labore</p>
      <p class="foot copy">Lorem ipsum dolor sit amet, consectetur adipisicing elit, sed do eiusmod tempor incididunt ut labore et dolore magna</p>
    </div>
    <div class="abs card" style="left:374px;top:658px">
      <div class="thumb" style="background:linear-gradient(135deg,#c9d43a,#6a6a55)" role="img" aria-label="Photo of track workers in high-visibility gear"></div>
      <p class="side copy">Lorem ipsum dolor sit amet, consectetur adipisicing elit, sed do eiusmod tempor incididunt ut labore</p>
      <p class="foot copy">Lorem ipsum dolor sit amet, consectetur adipisicing elit, sed do eiusmod tempor incididunt ut labore et dolore magna</p>
    </div>
    <div class="abs card" style="left:605px;top:658px">
      <div class="thumb" style="background:linear-gradient(135deg,#7a7d80,#2a3550)" role="img" aria-label="Photo of uniformed staff beside a freight wagon"></div>
      <p class="side copy">Lorem ipsum dolor sit amet, consectetur adipisicing elit, sed do eiusmod tempor incididunt ut labore</p>
      <p class="foot copy">Lorem ipsum dolor sit amet, consectetur adipisicing elit, sed do eiusmod tempor incididunt ut labore et dolore magna</p>
    </div>

    <div class="abs card" style="left:141px;top:808px">
      <div class="thumb" style="background:linear-gradient(135deg,#4f6b3c,#3c4a6a)" role="img" aria-label="Photo of a group of rail staff"></div>
      <p class="side copy">Lorem ipsum dolor sit amet, consectetur adipisicing elit, sed do eiusmod tempor incididunt ut labore</p>
      <p class="foot copy">Lorem ipsum dolor sit amet, consectetur adipisicing elit, sed do eiusmod tempor incididunt ut labore et dolore magna</p>
    </div>
    <div class="abs card" style="left:374px;top:808px">
      <div class="thumb" style="background:linear-gradient(135deg,#c9d43a,#6a6a55)" role="img" aria-label="Photo of track workers in high-visibility gear"></div>
      <p class="side copy">Lorem ipsum dolor sit amet, consectetur adipisicing elit, sed do eiusmod tempor incididunt ut labore</p>
      <p class="foot copy">Lorem ipsum dolor sit amet, consectetur adipisicing elit, sed do eiusmod tempor incididunt ut labore et dolore magna</p>
    </div>
    <div class="abs card" style="left:605px;top:808px">
      <div class="thumb" style="background:linear-gradient(135deg,#7a7d80,#2a3550)" role="img" aria-label="Photo of uniformed staff beside a freight wagon"></div>
      <p class="side copy">Lorem ipsum dolor sit amet, consectetur adipisicing elit, sed do eiusmod tempor incididunt ut labore</p>
      <p class="foot copy">Lorem ipsum dolor sit amet, consectetur adipisicing elit, sed do eiusmod tempor incididunt ut labore et dolore magna</p>
    </div>
  </section>

  <section class="partners">
    <div class="abs band" style="top:950px"></div>
    <h2 class="abs partners-title">PARTNERS</h2>
    <svg class="abs" style="left:140px;top:995px" width="680" height="110" viewBox="0 0 680 110" role="img" aria-label="Partner badges">
      <rect class="partner" x="20" y="16" width="64" height="22" rx="11"/>
      <circle class="partner" cx="185" cy="26" r="14"/>
      <rect class="partner" x="270" y="12" width="112" height="30" rx="4"/>
      <circle class="partner" cx="502" cy="26" r="18"/>
      <rect class="partner" x="560" y="12" width="100" height="30" rx="4"/>
      <circle class="partner" cx="50" cy="83" r="18"/>
      <rect class="partner" x="135" y="68" width="104" height="30" rx="4"/>
      <rect class="partner" x="328" y="68" width="72" height="30" rx="4"/>
      <circle class="partner" cx="505" cy="83" r="16"/>
      <rect class="partner" x="595" y="68" width="50" height="30" rx="4"/>
    </svg>
  </section>

  <footer>
    <div class="abs footer"></div>
    <div class="abs copyright">Copyright © 2011 Signalroll,</div>
    <div class="abs footer-nav">Home<span>|</span>How It Works<span>|</span>Prices<span>|</span>Our Customers<span>|</span>About Us<span>|</span>Contact</div>
  </footer>

</div>
</body>
</html>
```